The Assembly Hall Book Cover

This book cover will be used for both a eReader and a paperback book. The title of the book is "The Assembly Hall"   and "A Novel" should appear below that.  The title should be on the Front cover and on the spine. The author is Brant Malvory.. That also appears on the front cover and spine.
The book is political thriller about a runaway constitutional convention set in the United States, shortly after the first woman is elected president.  The cover should be graphic, attractive and depict the arc of the story. On the back panel of the book cover (the left side), we should see a depiction of a wheat field in the midwest, perhaps a road, leading to the spine and front cover. (The hero is a small town newspaper publisher from Nebraska.) The front cover morphs into a graphic image where the wheat shafts become arms and hands upraised in several iconic symbols, perhaps the two finger V for victory or peace sign, the black power raised fist, the aloha two finger sign, .. with at the center of the raised fists, a distinct fist holding a small American flag. The graphic image should grab the audience, and represent the power of the people to rise up and turn politics upside down.
I am writing a series of these political novels, so I want the graphic image here, while unique to be  able to be used in some sense in future novels. (See for example, the Miles Dunthorpe spy series published by Harrowgate Press.
I will want the final file to permit me to add a short description of the novel on the back cover, perhaps a short blurb from a review as well.

Updates
Project Deadline Extended
Reason: Current designs are good, with a few revisions and I need more time to give feedback, and make final decision.

Project Deadline Extended

Target Market(s)
Political junkies, people who like reading thrillers, and novels about law and politics, mass market e Reader and paperback audience.
Requirements
Must have
- The Assembly Hall (Title) on Front Cover and spine
- A Novel (under the title) on Front cover
- Brant Malvory on Front Cover and Spine
- Lanternfold Press on Spine

```html
<!DOCTYPE html>
<html lang="en">
<head>
<meta charset="utf-8">
<title>The Assembly Hall — Cover</title>
<link rel="stylesheet" href="https://fonts.googleapis.com/css2?family=Lilita+One&family=Comfortaa:wght@600&family=Quicksand:wght@500;700&family=Rubik:ital,wght@1,800&display=swap">
<style>
  :root {
    --sky-blue: #2f3fd6;
    --sky-violet: #6a3fc4;
    --sky-pink: #e8a7c8;
    --sky-cream: #fbf3e4;
    --gold: #f2c23c;
    --wheat: #d79a22;
    --wheat-dark: #a9701a;
    --title-red: #d2141c;
    --title-edge: #7a0a0e;
    --novel-blue: #3a2bc2;
    --tagline-red: #c3161d;
    --author-blue: #2a34d0;
    --hand-red: #c8171f;
    --page: #ffffff;
  }
  html, body {
    margin: 0;
    padding: 0;
    width: 869px;
    height: 1200px;
    overflow: hidden;
    background: var(--page);
  }
  .book {
    display: flex;
    width: 869px;
    height: 1200px;
  }

  /* ---------- Spine ---------- */
  .spine {
    position: relative;
    flex: 0 0 92px;
    height: 1200px;
    overflow: hidden;
    background: linear-gradient(180deg, var(--sky-blue) 0%, var(--sky-violet) 30%, var(--sky-pink) 58%, var(--sky-cream) 74%, var(--gold) 84%, var(--wheat) 100%);
    box-shadow: inset -6px 0 10px rgba(0,0,0,0.18);
    display: flex;
    flex-direction: column;
    align-items: center;
    padding: 40px 0 30px;
    box-sizing: border-box;
  }
  .spine-text {
    writing-mode: vertical-rl;
    margin: 0;
    white-space: nowrap;
  }
  .spine-title {
    font-family: "Lilita One", sans-serif;
    font-size: 46px;
    color: var(--title-red);
    -webkit-text-stroke: 2px var(--title-edge);
    paint-order: stroke fill;
    text-shadow: 2px 2px 0 #ffffff;
    letter-spacing: 1px;
  }
  .spine-author {
    margin-top: 70px;
    font-family: "Quicksand", sans-serif;
    font-weight: 700;
    font-size: 26px;
    letter-spacing: 2px;
    color: #ffffff;
  }
  .spine-subtitle {
    margin-top: auto;
    font-family: "Rubik", sans-serif;
    font-style: italic;
    font-weight: 800;
    font-size: 24px;
    color: var(--novel-blue);
  }
  .spine-press {
    margin-top: 26px;
    font-family: "Quicksand", sans-serif;
    font-weight: 700;
    font-size: 15px;
    letter-spacing: 1px;
    color: #4a2a06;
  }

  /* ---------- Front cover ---------- */
  .front {
    position: relative;
    flex: 1 1 auto;
    height: 1200px;
    overflow: hidden;
    background: linear-gradient(160deg, var(--sky-blue) 0%, var(--sky-violet) 28%, var(--sky-pink) 52%, var(--sky-cream) 68%, var(--gold) 100%);
  }
  .rays {
    position: absolute;
    inset: 0;
    width: 100%;
    height: 100%;
  }
  .wheat-field {
    position: absolute;
    left: 0;
    bottom: 0;
    width: 100%;
    height: 380px;
    background: linear-gradient(180deg, rgba(242,194,60,0) 0%, var(--gold) 22%, var(--wheat) 60%, var(--wheat-dark) 100%);
  }
  .raised-hand {
    position: absolute;
    left: 555px;
    top: 400px;
    width: 200px;
    height: 610px;
    background: linear-gradient(180deg, var(--hand-red), #a01018);
    border-radius: 80px 80px 30px 30px;
    opacity: 0.92;
  }
  .title {
    position: absolute;
    left: 40px;
    top: 150px;
    margin: 0;
    font-family: "Lilita One", sans-serif;
    font-weight: 400;
    color: var(--title-red);
    -webkit-text-stroke: 3px var(--title-edge);
    paint-order: stroke fill;
    text-shadow: 4px 5px 0 #ffffff, 6px 8px 10px rgba(0,0,0,0.25);
    line-height: 0.95;
    white-space: nowrap;
    transform: rotate(-4deg);
    transform-origin: left center;
  }
  .title-lead {
    display: block;
    font-size: 58px;
    margin-left: 20px;
  }
  .title-main {
    display: block;
    font-size: 88px;
    letter-spacing: 1px;
  }
  .subtitle {
    position: absolute;
    left: 330px;
    top: 330px;
    margin: 0;
    font-family: "Rubik", sans-serif;
    font-style: italic;
    font-weight: 800;
    font-size: 58px;
    color: var(--novel-blue);
    text-shadow: 3px 3px 0 #ffffff;
    transform: rotate(-4deg);
  }
  .tagline {
    position: absolute;
    left: 150px;
    top: 470px;
    margin: 0;
    font-family: "Comfortaa", sans-serif;
    font-weight: 600;
    font-size: 40px;
    line-height: 1.05;
    color: var(--tagline-red);
    text-align: right;
    transform: rotate(-6deg);
  }
  .author {
    position: absolute;
    left: 0;
    right: 0;
    top: 1030px;
    margin: 0;
    text-align: center;
    font-family: "Quicksand", sans-serif;
    font-weight: 500;
    font-size: 74px;
    letter-spacing: 1px;
    color: var(--author-blue);
    -webkit-text-stroke: 2px #ffffff;
    paint-order: stroke fill;
    transform: rotate(-3deg);
  }
</style>
</head>
<body>
  <div class="book">
    <aside class="spine">
      <p class="spine-text spine-title">THE ASSEMBLY HALL</p>
      <p class="spine-text spine-author">BRANT MALVORY</p>
      <p class="spine-text spine-subtitle">A NOVEL</p>
      <p class="spine-text spine-press">Lanternfold Press</p>
    </aside>

    <main class="front">
      <svg class="rays" viewBox="0 0 777 1200" preserveAspectRatio="none" aria-hidden="true">
        <g fill="#ffffff" opacity="0.22">
          <polygon points="680,900 -100,0 120,0"/>
          <polygon points="680,900 250,0 430,0"/>
          <polygon points="680,900 560,0 700,0"/>
          <polygon points="680,900 777,80 777,260"/>
          <polygon points="680,900 0,380 0,560"/>
          <polygon points="680,900 0,760 0,880"/>
        </g>
        <g fill="#ffffff" opacity="0.35">
          <polygon points="330,80 340,108 370,108 346,125 355,153 330,136 305,153 314,125 290,108 320,108"/>
          <polygon points="70,560 78,582 102,582 83,596 90,618 70,604 50,618 57,596 38,582 62,582"/>
        </g>
      </svg>

      <div class="wheat-field" role="img" aria-label="Illustration of golden Midwest wheat stalks rising along the bottom of the cover"></div>
      <div class="raised-hand" role="img" aria-label="Graphic of a red raised hand making a two-finger V sign, rising out of the wheat"></div>

      <h1 class="title">
        <span class="title-lead">THE</span>
        <span class="title-main">ASSEMBLY HALL</span>
      </h1>
      <p class="subtitle">A Novel</p>
      <p class="tagline">a runaway<br>constitutional<br>convention</p>
      <p class="author">BRANT MALVORY</p>
    </main>
  </div>
</body>
</html>
```